Marlow Hire Business Card for recruitment company

We are looking for a Business Card Design that incorporates our personal details and our busines name and logo. We are a specialized search consultancy that recruit Property and Construction professionals.
We would like a business card that stands out and is appealing to the Construction and Property industry as well.

Target Market(s)

people in the construction and property industry

Contact Information for Business Card

Business Name and logo

Font styles to use
Serif

Colors
0094D4
00A9DD
6FCCEA
C7EBF8
E9F6FB

Requirements
Must have
• Business name and logo as well as contact details
Should not have
• No photos of us please

```html
<!DOCTYPE html>
<html lang="en">
<head>
<meta charset="utf-8">
<title>Marlow Hire Business Card</title>
<link rel="stylesheet" href="https://fonts.googleapis.com/css2?family=Montserrat:wght@400;500;600&display=swap">
<style>
  :root {
    --stage: #d0d0d0;
    --ink: #053b4e;
    --paper: #ffffff;
    --faint: rgba(255, 255, 255, 0.08);
    --shadow: rgba(0, 0, 0, 0.35);
  }
  * { margin: 0; padding: 0; box-sizing: border-box; }
  html, body { width: 900px; height: 1200px; overflow: hidden; }
  body {
    background: var(--stage);
    font-family: "Montserrat", sans-serif;
    position: relative;
  }
  .card {
    position: absolute;
    left: 80px;
    width: 742px;
    height: 441px;
    overflow: hidden;
    box-shadow: 0 6px 18px var(--shadow);
  }
  .card--front { top: 131px; background: var(--paper); }
  .card--back { top: 638px; height: 440px; background: var(--ink); }

  .wordmark {
    position: absolute;
    left: 0; right: 0;
    text-align: center;
    font-weight: 500;
    font-size: 62px;
    letter-spacing: 4px;
    line-height: 1;
    text-transform: uppercase;
  }
  .card--front .wordmark { top: 78px; color: var(--ink); }
  .card--back .wordmark { top: 193px; color: var(--paper); z-index: 2; }

  .band {
    position: absolute;
    left: 0; top: 202px;
    width: 100%; height: 194px;
    background: var(--ink);
  }
  .base-strip {
    position: absolute;
    left: 0; bottom: 0;
    width: 100%; height: 12px;
    background: var(--ink);
  }
  .holder { position: absolute; left: 43px; top: 229px; color: var(--paper); }
  .holder__name { font-weight: 600; font-size: 25px; line-height: 30px; letter-spacing: 0.3px; }
  .holder__role { font-weight: 400; font-size: 16px; line-height: 22px; margin-top: 0; }

  .contacts {
    position: absolute;
    left: 43px; top: 297px;
    list-style: none;
    color: var(--paper);
    font-size: 16px;
  }
  .contacts li { display: flex; align-items: center; height: 24.5px; }
  .contacts svg { width: 14px; height: 14px; margin-right: 9px; fill: var(--paper); flex: none; }

  .emblem-spot {
    position: absolute;
    left: 484px; top: 191px;
    width: 216px; height: 216px;
    border-radius: 50%;
    background: var(--paper);
  }
  .back-circle {
    position: absolute;
    left: 355px; top: 40px;
    width: 390px; height: 390px;
    border-radius: 50%;
    background: var(--faint);
  }
</style>
</head>
<body>
  <section class="card card--front">
    <div class="wordmark">Marlow Hire</div>
    <div class="band"></div>
    <div class="holder">
      <p class="holder__name">Dana Ellery</p>
      <p class="holder__role">Owner/ Designer</p>
    </div>
    <ul class="contacts">
      <li><svg viewBox="0 0 16 16" aria-hidden="true"><path d="M1 6c0-2 3-4 7-4s7 2 7 4v1h-4V5.5H5V7H1zM4 8h8l2 5H2z"/></svg>(555) 014-2290</li>
      <li><svg viewBox="0 0 16 16" aria-hidden="true"><path d="M1 4h14v1L8 9 1 5zM1 6.5l7 4 7-4V12H1z"/></svg>info@marlowhire.com</li>
      <li><svg viewBox="0 0 16 16" aria-hidden="true"><circle cx="8" cy="8" r="6.5"/><path d="M5 4.5l2 1-1 2 2 1v2l-2 2-1-3-2-1zM10 3.5l2 2-1 2-2-1z" fill="#053b4e"/></svg>www.marlowhire.com</li>
    </ul>
    <div class="emblem-spot"></div>
    <div class="base-strip"></div>
  </section>

  <section class="card card--back">
    <div class="back-circle"></div>
    <div class="wordmark">Marlow Hire</div>
  </section>
</body>
</html>
```